Serial Entrepreneur Business Card: 4 Logo Design

I am a serial entrepreneur and a full time mechanical engineer. I have four businesses. I would like to display them all on one business card.
*Please see the attached PDF for the design requirements*

www.KelbroNest.com

Businesses
-KelbroNest
-Quiet Lantern Properties
-Torlen Products
-Drosk Harbor Cast

Target Market(s)

Clients, Entrepreneurs, Associates, really anyone. Should be very professional.

Industry/Entity Type

Entrepreneur

Contact Information for Business Card

3.5" x 2" Standard Business Card Size
** Please review the attached requirement PDF for in depth detail on what I am expecting**

Font styles to use
Sans Serif

Requirements
Must have
• My personal contact information:
• First Name: Dae hwan
• Last Name: Pellow
• Nick Name: Riko
• Address: 83 Tolmer Court, Garfield NJ 07392
• Phone Number: 201-574-2916
• Email: RikodPellow@mailnest.example
• Website: www.KelbroNest.com
• All Four Logos of the Companies I own:
• -KelbroNest
• -Quiet Lantern Properties
• -Torlen Products
• -Drosk Harbor Cast
• My Professions:
• -Prototyping Engineer
• -Real Estate Investor
• -Financial Blogger
• -Video Podcaster
• -Online Retail Seller
Nice to have
• If it fits, please include the website for each logo, if there is more space please include the email for each.
• It might be nice to have the QX GUILD Logo, or TOVRA logo for my full-time job. But only if it fits.

```html
<!DOCTYPE html>
<html lang="en">
<head>
<meta charset="utf-8">
<title>Dae hwan "Riko" Pellow – Business Card</title>
<link rel="stylesheet" href="https://fonts.googleapis.com/css2?family=Roboto+Condensed:wght@300;400;700&family=Oswald:wght@600&display=swap">
<style>
  :root {
    --bg: #e9e4dc;
    --card: #ffffff;
    --ink: #2b2b2b;
    --ink-soft: #3a3a3a;
    --green: #1f8a1f;
    --grey: #7a7a7a;
    --black: #222222;
  }
  * { margin: 0; padding: 0; box-sizing: border-box; }
  html, body { width: 790px; height: 1200px; overflow: hidden; }
  body { background: var(--bg); font-family: "Roboto Condensed", Arial, sans-serif; color: var(--ink); position: relative; }

  .card { position: absolute; background: var(--card); box-shadow: 0 4px 14px rgba(0,0,0,.18); overflow: hidden; }
  .card-back { left: 215px; top: 90px; width: 351px; height: 618px; }
  .card-front { left: 84px; top: 780px; width: 617px; height: 351px; }

  .accent-band {
    position: absolute; left: 0; right: 0; bottom: 0;
    background: linear-gradient(90deg, var(--grey) 0%, var(--green) 50%, var(--black) 100%);
  }
  .card-back .accent-band { height: 27px; }
  .card-front .accent-band { height: 21px; }

  /* back: business list */
  .venture { position: absolute; left: 0; width: 100%; text-align: center; }
  .venture-mark {
    display: flex; align-items: center; justify-content: center; gap: 8px;
    font-weight: 700; font-size: 24px; line-height: 1;
  }
  .venture-mark .square { width: 14px; height: 14px; display: inline-block; flex: none; }
  .mark-green { color: var(--green); }
  .mark-green .square { background: var(--green); }
  .mark-dark { color: var(--black); }
  .mark-dark .square { background: var(--black); }
  .venture-url { font-weight: 300; font-size: 15px; margin-top: 12px; color: var(--ink-soft); }
  .venture-role { font-family: "Oswald", sans-serif; font-weight: 600; font-size: 12px; margin-top: 3px; }
  .venture-email { font-weight: 400; font-size: 12px; margin-top: 3px; color: var(--ink-soft); }

  /* front: personal details */
  .owner-name { position: absolute; left: 62px; top: 47px; font-family: "Oswald", sans-serif; font-weight: 600; font-size: 16px; letter-spacing: .3px; color: var(--ink); }
  .contact-list { position: absolute; left: 62px; top: 90px; list-style: none; }
  .contact-list li { display: flex; align-items: center; height: 28px; font-weight: 300; font-size: 18.5px; color: var(--ink-soft); }
  .contact-list svg { width: 18px; height: 20px; margin-right: 13px; flex: none; }
  .profession-list { position: absolute; left: 399px; top: 89px; list-style: none; }
  .profession-list li { font-weight: 300; font-size: 17.5px; height: 22.8px; color: var(--ink-soft); }
  .profession-list li::before { content: "•"; color: var(--green); margin-right: 8px; font-weight: 700; }

  .venture-row { position: absolute; left: 70px; right: 80px; top: 264px; display: flex; justify-content: space-between; }
  .venture-row .venture-mark { font-size: 16px; gap: 6px; }
  .venture-row .square { width: 11px; height: 11px; }
</style>
</head>
<body>

<section class="card card-back" aria-label="Card back: businesses">
  <div class="venture" style="top:56px">
    <div class="venture-mark mark-green"><span class="square"></span>KelbroNest</div>
    <p class="venture-url">www.KelbroNest.com</p>
    <p class="venture-role">Financial Blogger</p>
    <p class="venture-email">Riko@KelbroNest.com</p>
  </div>
  <div class="venture" style="top:214px">
    <div class="venture-mark mark-dark"><span class="square"></span>Torlen Products</div>
    <p class="venture-url">www.TorlenProducts.com</p>
    <p class="venture-role">Online Retail Seller</p>
    <p class="venture-email">Sales@TorlenProducts.com</p>
  </div>
  <div class="venture" style="top:359px">
    <div class="venture-mark mark-green"><span class="square"></span>Drosk Harbor Cast</div>
    <p class="venture-url">www.DroskHarborCast.com</p>
    <p class="venture-role">Vlogger</p>
    <p class="venture-email">Media@DroskHarborCast.com</p>
  </div>
  <div class="venture" style="top:482px">
    <div class="venture-mark mark-dark"><span class="square"></span>Quiet Lantern Properties</div>
    <p class="venture-url">www.QuietLanternProperties.com</p>
    <p class="venture-role">Real Estate Investing</p>
    <p class="venture-email">Riko@QuietLanternProperties.com</p>
  </div>
  <div class="accent-band" role="img" aria-label="Decorative grey, green and black band"></div>
</section>

<section class="card card-front" aria-label="Card front: contact details">
  <h1 class="owner-name">DAE HWAN «RIKO» PELLOW</h1>

  <ul class="contact-list">
    <li>
      <svg viewBox="0 0 18 20" aria-hidden="true"><rect x="3" y="1" width="12" height="18" rx="2" fill="none" stroke="var(--green)" stroke-width="2"/><circle cx="9" cy="15.5" r="1.2" fill="var(--green)"/></svg>
      201-574-2916
    </li>
    <li>
      <svg viewBox="0 0 18 20" aria-hidden="true"><rect x="1" y="5" width="16" height="11" fill="none" stroke="var(--green)" stroke-width="1.8"/><path d="M1 5 L9 11 L17 5" fill="none" stroke="var(--green)" stroke-width="1.8"/></svg>
      RikodPellow@mailnest.example
    </li>
    <li>
      <svg viewBox="0 0 18 20" aria-hidden="true"><circle cx="9" cy="10" r="8" fill="none" stroke="var(--green)" stroke-width="1.8"/><ellipse cx="9" cy="10" rx="3.5" ry="8" fill="none" stroke="var(--green)" stroke-width="1.4"/><path d="M1 10 H17 M2.5 6 H15.5 M2.5 14 H15.5" stroke="var(--green)" stroke-width="1.2"/></svg>
      www.KelbroNest.com
    </li>
    <li>
      <svg viewBox="0 0 18 20" aria-hidden="true"><path d="M9 19 C9 19 2 11 2 7.5 A7 7 0 0 1 16 7.5 C16 11 9 19 9 19 Z" fill="var(--green)"/><circle cx="9" cy="7.5" r="2.6" fill="#fff"/></svg>
      83 Tolmer Court, Garfield NJ 07392
    </li>
  </ul>

  <ul class="profession-list">
    <li>Prototyping Engineer</li>
    <li>Real Estate Investor</li>
    <li>Financial Blogger</li>
    <li>Video Podcaster</li>
    <li>Online Retail Seller</li>
  </ul>

  <div class="venture-row">
    <div class="venture-mark mark-dark"><span class="square"></span>KelbroNest</div>
    <div class="venture-mark mark-green"><span class="square"></span>Drosk Harbor Cast</div>
    <div class="venture-mark mark-dark"><span class="square"></span>Quiet Lantern</div>
    <div class="venture-mark mark-dark"><span class="square"></span>Torlen</div>
  </div>

  <div class="accent-band" role="img" aria-label="Decorative grey, green and black band"></div>
</section>

</body>
</html>
```